Bref créative
Business Cards and Stationary for Conference App Company
Kalvornet
Modern
Lars Henrik Dalsgaard
Partner
Solbærvej 254
DK-4130 Vestrup
lhd@kalvornet.example
kalvornet.example

```html
<!DOCTYPE html>
<html lang="en">
<head>
<meta charset="utf-8">
<title>Kalvornet business cards</title>
<link rel="stylesheet" href="https://fonts.googleapis.com/css2?family=Open+Sans:ital,wght@0,400;0,600;1,400&display=swap">
<style>
  :root {
    --orange: #f6a623;
    --orange-deep: #ee9a12;
    --grey: #7d7f82;
    --grey-light: #b9bbbe;
    --white: #ffffff;
    --stage: #dcdcdc;
  }
  * { margin: 0; padding: 0; box-sizing: border-box; }
  html, body { width: 1200px; height: 987px; overflow: hidden; }
  body {
    background: var(--stage);
    font-family: "Open Sans", Arial, sans-serif;
    position: relative;
  }
  .card {
    position: absolute;
    width: 620px;
    height: 400px;
    border-radius: 22px;
    overflow: hidden;
  }
  /* Back side */
  .card-back {
    left: 90px;
    top: 80px;
    background: var(--orange);
  }
  .card-back .brand {
    position: absolute;
    left: 0; right: 0; top: 130px;
    display: flex; justify-content: center; align-items: center; gap: 16px;
  }
  .card-back .brand-square {
    width: 44px; height: 44px; background: var(--white);
  }
  .card-back .brand-name {
    color: var(--white); font-size: 44px; font-weight: 600; letter-spacing: 0.5px;
  }
  .card-back .web {
    position: absolute; left: 0; right: 0; top: 238px;
    text-align: center; color: var(--white);
    font-size: 24px; font-style: italic; letter-spacing: 6px;
  }
  /* Front side */
  .card-front {
    left: 490px;
    top: 510px;
    background: var(--white);
  }
  .card-front svg.waves { position: absolute; left: 0; top: 0; }
  .card-front .brand {
    position: absolute; left: 200px; top: 56px;
    display: flex; align-items: center; gap: 12px;
  }
  .card-front .brand-square { width: 38px; height: 38px; background: var(--grey); }
  .card-front .brand-name { color: var(--orange-deep); font-size: 40px; font-weight: 400; }
  .card-front .tagline {
    position: absolute; left: 250px; top: 106px;
    color: var(--grey); font-size: 19px;
  }
  .card-front .person { position: absolute; left: 270px; top: 142px; }
  .card-front .person-name { color: var(--orange-deep); font-size: 17px; font-weight: 600; }
  .card-front .person-role { color: var(--grey); font-size: 14px; margin-top: 2px; padding-left: 70px; }
  .card-front .address {
    position: absolute; left: 170px; top: 202px;
    color: var(--grey); font-size: 14px; line-height: 21px; text-align: right; width: 150px;
  }
  .card-front .divider {
    position: absolute; left: 336px; top: 200px; width: 1px; height: 68px; background: var(--grey-light);
  }
  .card-front .contacts {
    position: absolute; left: 348px; top: 196px;
    list-style: none; color: var(--grey); font-size: 14px;
  }
  .card-front .contacts li { display: flex; align-items: center; gap: 8px; height: 24px; }
  .card-front .contacts svg { flex: none; }
</style>
</head>
<body>

<section class="card card-back" aria-label="Card back">
  <div class="brand">
    <span class="brand-square"></span>
    <span class="brand-name">Kalvornet</span>
  </div>
  <p class="web">www.kalvornet.example</p>
</section>

<section class="card card-front" aria-label="Card front">
  <svg class="waves" width="620" height="400" viewBox="0 0 620 400" aria-hidden="true">
    <path d="M0 280 C 160 300, 330 330, 460 300 C 540 282, 590 255, 620 235 L620 400 L0 400 Z" fill="var(--orange)"/>
    <path d="M0 282 C 180 318, 360 345, 480 312 C 550 292, 595 262, 620 240 L620 252 C 590 276, 548 302, 482 322 C 360 356, 180 330, 0 296 Z" fill="var(--white)"/>
    <path d="M40 298 C 210 330, 380 350, 500 318 C 560 302, 600 276, 620 258" fill="none" stroke="var(--grey)" stroke-width="6" stroke-linecap="round"/>
  </svg>

  <div class="brand">
    <span class="brand-square"></span>
    <span class="brand-name">Kalvornet</span>
  </div>
  <p class="tagline">Meetings Made Simple</p>

  <div class="person">
    <p class="person-name">Lars Henrik Dalsgaard</p>
    <p class="person-role">Partner</p>
  </div>

  <p class="address">Solbærvej 254<br>DK-4130 Vestrup</p>
  <span class="divider"></span>

  <ul class="contacts">
    <li>
      <svg width="14" height="14" viewBox="0 0 14 14" aria-hidden="true"><circle cx="7" cy="7" r="7" fill="var(--orange)"/><path d="M4.5 3.5 L6 5.5 L5.2 6.4 C5.8 7.6 6.6 8.4 7.6 8.9 L8.5 8 L10.5 9.5 L9.6 10.6 C7 10.4 3.6 7 3.4 4.4 Z" fill="var(--white)"/></svg>
      45 21604872
    </li>
    <li>
      <svg width="14" height="14" viewBox="0 0 14 14" aria-hidden="true"><circle cx="7" cy="7" r="7" fill="var(--orange)"/><rect x="3.5" y="4.5" width="7" height="5" fill="none" stroke="var(--white)" stroke-width="1"/><path d="M3.5 4.5 L7 7.3 L10.5 4.5" fill="none" stroke="var(--white)" stroke-width="1"/></svg>
      lhd@kalvornet.example
    </li>
    <li>
      <svg width="14" height="14" viewBox="0 0 14 14" aria-hidden="true"><circle cx="7" cy="7" r="7" fill="var(--orange)"/><circle cx="7" cy="7" r="3.6" fill="none" stroke="var(--white)" stroke-width="1"/><path d="M3.4 7 H10.6 M7 3.4 V10.6" stroke="var(--white)" stroke-width="0.8"/></svg>
      www.kalvornet.example
    </li>
  </ul>
</section>

</body>
</html>
```